Marlow Bay Kestrel Arrivals Flyer

A 2 sided DL size flyer. (Approx 20cm long by 10cm wide)
That has logo and blurb about company on front. On back details of Kestrel arrivals package, trademark, contact details and license numbers.
We feel we need to see the text on the flyer design and then make some changes so there will be some back and forth about written content. There may be a reduction in the amount of text we want for the blurb about the company but the rest is mandatory.
Our logo is blue and green, we do not want a white flyer with black text as feel this looks homemade so we need your suggestions about what colour the text and flyer could be.
We want the flyer to look clean and modern. It will go on a stand at an immigration fair and will be sent in the post and via email to clients. We will need posters at a later stage.
Migrants
It Company

```html
<!DOCTYPE html>
<html lang="en">
<head>
<meta charset="utf-8">
<title>Marlow Bay Kestrel Arrivals Banner</title>
<link href="https://fonts.googleapis.com/css2?family=Russo+One&family=Audiowide&family=Roboto+Condensed:wght@700&family=Open+Sans:wght@300;400&display=swap" rel="stylesheet">
<style>
  :root{
    --page:#9aa3ad;
    --blue:#0e63ad;
    --blue-deep:#0a4d8f;
    --logo-blue:#1a74c9;
    --green:#3ed33f;
    --green-dark:#2fb53a;
    --navy:#0c3f7a;
    --white:#ffffff;
    --grey:#e3e6e9;
    --ink:#1c1c1c;
  }
  html,body{margin:0;padding:0;width:1200px;height:1111px;overflow:hidden;background:var(--page);}
  .banner{position:absolute;left:332px;top:20px;width:598px;height:1195px;transform:scale(0.896);transform-origin:0 0;background:var(--white);overflow:hidden;box-shadow:0 6px 18px rgba(0,0,0,.25);}
  .banner-bg{position:absolute;left:0;top:0;}
  .layer{position:absolute;}
  .logo-mark{left:60px;top:41px;width:100px;height:100px;border:8px solid var(--green);border-radius:50%;box-sizing:border-box;}
  .logo-divider{left:194px;top:38px;width:2px;height:118px;background:var(--ink);}
  .logo-name{left:206px;top:40px;font-family:"Russo One",sans-serif;font-size:34px;line-height:40px;color:var(--logo-blue);margin:0;}
  .logo-tagline{left:208px;top:118px;font-family:"Open Sans",sans-serif;font-size:19px;letter-spacing:5.4px;color:var(--ink);}
  .scenery{left:0;top:150px;width:598px;height:430px;}
  .headline{left:0;width:598px;top:538px;text-align:center;font-family:"Russo One",sans-serif;font-size:45px;letter-spacing:1px;color:var(--green);margin:0;}
  .subline{left:46px;top:600px;width:506px;height:44px;border-radius:22px;background:linear-gradient(#fff,#d7dbe0);text-align:center;font-family:"Roboto Condensed",sans-serif;font-weight:700;font-size:26px;line-height:44px;color:var(--navy);box-shadow:0 8px 12px rgba(0,0,0,.25);}
  .advisers-box{left:28px;top:693px;width:538px;height:70px;border:1px solid rgba(255,255,255,.55);}
  .advisers-lead{left:0;width:598px;top:675px;text-align:center;font-family:"Open Sans",sans-serif;font-weight:300;font-size:28px;color:var(--white);}
  .advisers-lead span{background:var(--blue);padding:0 12px;}
  .advisers-title{left:0;width:598px;top:712px;text-align:center;font-family:"Audiowide",sans-serif;font-size:36px;color:var(--green);}
  .contact-list{left:44px;top:815px;margin:0;padding:0;list-style:none;font-family:"Open Sans",sans-serif;font-size:21px;color:var(--white);}
  .contact-list li{display:flex;align-items:center;height:33px;}
  .contact-list svg{margin-right:11px;}
  .contact-rule{left:358px;top:818px;width:1px;height:74px;background:rgba(255,255,255,.3);}
  .badge{left:430px;top:785px;width:128px;height:128px;border-radius:50%;background:#c6d4c0;border:6px solid var(--green);box-sizing:border-box;box-shadow:0 0 0 3px #e0e6e0 inset;}
  .adviser{top:934px;height:54px;border:1.5px solid var(--white);border-radius:27px;text-align:center;color:var(--white);font-family:"Roboto Condensed",sans-serif;box-sizing:border-box;}
  .adviser strong{display:block;font-size:20px;line-height:24px;padding-top:5px;font-weight:400;}
  .adviser small{display:block;font-size:12px;line-height:16px;}
  .adviser-one{left:30px;width:260px;}
  .adviser-two{left:306px;width:262px;}
  .closing{left:0;width:598px;top:1100px;text-align:center;font-family:"Russo One",sans-serif;font-size:30px;line-height:34px;letter-spacing:1px;margin:0;}
  .closing .top{color:var(--navy);display:block;}
  .closing .bottom{color:var(--green-dark);display:block;}
  .closing-rule{top:1132px;width:86px;height:1px;background:var(--navy);}
</style>
</head>
<body>
<div class="banner">
  <svg class="banner-bg" width="598" height="1195" viewBox="0 0 598 1195">
    <defs>
      <linearGradient id="bodyBlue" x1="0" y1="0" x2="0" y2="1">
        <stop offset="0" stop-color="#1066b3"/>
        <stop offset="1" stop-color="#0a4f94"/>
      </linearGradient>
      <linearGradient id="footGrey" x1="0" y1="0" x2="1" y2="0">
        <stop offset="0" stop-color="#d4d8dc"/>
        <stop offset=".5" stop-color="#f4f5f6"/>
        <stop offset="1" stop-color="#d4d8dc"/>
      </linearGradient>
    </defs>
    <rect width="598" height="1195" fill="url(#footGrey)"/>
    <rect width="598" height="200" fill="#ffffff"/>
    <path d="M0,550 Q260,440 598,500 L598,1000 Q300,1085 0,1010 Z" fill="url(#bodyBlue)"/>
    <path d="M0,548 Q260,438 598,498 L598,512 Q300,462 0,570 Z" fill="#3ed33f"/>
    <path d="M0,1008 Q300,1082 598,998 L598,1016 Q300,1098 0,1022 Z" fill="#3ed33f"/>
  </svg>

  <div class="layer scenery" role="img" aria-label="Landscape photo of a blue lake with mountains and green vineyard rows" style="background:linear-gradient(180deg,rgba(255,255,255,1) 0%,#9cc9ef 14%,#4f82b8 34%,#2a5f9e 48%,#2f6f3a 62%,#5fae3a 82%,rgba(62,160,60,0) 100%);"></div>

  <div class="layer logo-mark"></div>
  <div class="layer logo-divider"></div>
  <h1 class="layer logo-name">Marlow Bay<br>Kestrel Arrivals</h1>
  <div class="layer logo-tagline">Immigration Advice</div>

  <h2 class="layer headline">NEW ZEALAND VISAS</h2>
  <div class="layer subline">Study, Visit or Work in Beautiful New Zealand</div>

  <div class="layer advisers-box"></div>
  <div class="layer advisers-lead"><span>Experienced and Friendly</span></div>
  <div class="layer advisers-title">IMMIGRATION ADVISERS</div>

  <ul class="layer contact-list">
    <li>
      <svg width="20" height="20" viewBox="0 0 20 20"><circle cx="10" cy="10" r="10" fill="#fff"/><rect x="5" y="6.5" width="10" height="7" fill="none" stroke="#0e63ad" stroke-width="1.4"/><path d="M5 6.5 L10 10.5 L15 6.5" fill="none" stroke="#0e63ad" stroke-width="1.4"/></svg>
      hello@marlowbaykestrel.com
    </li>
    <li>
      <svg width="20" height="20" viewBox="0 0 20 20"><circle cx="10" cy="10" r="10" fill="#fff"/><circle cx="10" cy="10" r="5.5" fill="none" stroke="#0e63ad" stroke-width="1.3"/><path d="M4.5 10 H15.5 M10 4.5 Q7 10 10 15.5 Q13 10 10 4.5" fill="none" stroke="#0e63ad" stroke-width="1.1"/></svg>
      www.marlowbaykestrel.com
    </li>
  </ul>
  <div class="layer contact-rule"></div>
  <div class="layer badge"></div>

  <div class="layer adviser adviser-one"><strong>Maren +64 21480736</strong><small>License No. 201408517</small></div>
  <div class="layer adviser adviser-two"><strong>Talia +64 2109573618</strong><small>License No. 201702394</small></div>

  <div class="layer closing-rule" style="left:0;"></div>
  <div class="layer closing-rule" style="left:512px;"></div>
  <p class="layer closing"><span class="top">WE FACILITATE FAST AND</span><span class="bottom">PROBLEM FREE VISAS</span></p>
</div>
</body>
</html>
```